Website for IT consulting Company

I need a website upgrade, the existing site content is ok, I would also like to add a testimonial page, the site should be something that is easy for us to update content. You use the content from www.kavnex.com as an example. I will also post update logo and artwork. I also need a contact form with some type of validation or captcha.

I added Coded to the Project

Please omit Address maps

Target Market(s)

small business, service oriented companies. We provide IT Consulting, support and mangement

Industry/Entity Type

Information Technology

Coding

Coded - Design and coding required

Number of Pages Required

1 page

Font styles to use
Serif
Sans Serif

Requirements
Must have
• Contain logo attached, and content from existing web site www.kavnex.com.
• Also need to update content easily, and be movable to different platforms.
• There is a catch phrase
• "Let us worry about your technology…” “ so you don’t have to!”
• Should be included.
Nice to have
• Testimonial page, Project page where we can post new and past projects and pictures
Should not have
• none

```html
<!DOCTYPE html>
<html lang="en">
<head>
<meta charset="utf-8">
<title>KAVNEX — Customer Testimonials</title>
<link href="https://fonts.googleapis.com/css2?family=Roboto:ital,wght@0,400;0,500;1,400&display=swap" rel="stylesheet">
<style>
:root{
  --accent:#f7941d;
  --ink:#2b2b2b;
  --body:#444;
  --muted:#8a8a8a;
  --page:#f4f4f4;
  --card:#ffffff;
  --footer:#2b323d;
  --footer-line:#3d4551;
  --footer-text:#d8dbe0;
}
*{box-sizing:border-box;margin:0;padding:0}
html,body{width:998px;height:1200px;overflow:hidden}
body{font-family:'Roboto',sans-serif;background:var(--page);color:var(--body);position:relative}

.site-header{position:absolute;top:0;left:0;width:998px;height:58px;background:#fff;border-bottom:1px solid #e6e6e6}
.brand{position:absolute;left:74px;top:17px;display:flex;align-items:center;gap:7px;font-size:22px;font-weight:500;color:var(--accent);letter-spacing:1px}
.brand-square{width:18px;height:18px;background:var(--accent)}
.main-nav{position:absolute;top:0;left:443px;height:58px;display:flex;font-size:11px;color:var(--ink)}
.main-nav a{color:inherit;text-decoration:none;line-height:62px;margin-right:27px;position:relative}
.main-nav a.active{color:var(--accent)}
.main-nav a.active::before{content:"";position:absolute;left:0;right:0;top:0;height:2px;background:var(--accent)}
.search-icon{position:absolute;left:912px;top:24px}

.page-hero{position:absolute;top:58px;left:0;width:998px;height:80px;background:linear-gradient(90deg,#8e948f 0%,#b7bcc0 30%,#6f7a8c 55%,#c9ccd0 80%,#a9a6a4 100%)}
.page-hero h1{position:absolute;left:73px;top:30px;font-size:22px;font-weight:400;color:#fff}
.breadcrumb{position:absolute;right:73px;top:37px;font-size:11px;color:#fff}
.breadcrumb span{margin:0 9px}

.testimonials{position:absolute;top:181px;left:74px;width:851px;display:grid;grid-template-columns:270px 270px 270px;column-gap:21px;row-gap:17px}
.testimonial{background:var(--card);height:183px;padding:27px 26px 0;position:relative;box-shadow:0 1px 2px rgba(0,0,0,.04)}
.testimonial p{font-size:10.6px;line-height:18.5px;color:var(--body)}
.testimonial .tag{color:var(--accent)}
.author{display:flex;align-items:center;margin-top:14px}
.avatar{width:44px;height:44px;border-radius:50%;margin-right:16px;flex:none}
.author-name{font-size:11.5px;font-weight:500;color:var(--ink)}
.author-handle{font-size:9.5px;font-style:italic;color:var(--muted);margin-top:3px}
.quote-mark{position:absolute;right:20px;bottom:18px}

.view-more{position:absolute;left:452px;top:793px;width:95px;height:36px;background:var(--accent);color:#fff;font-size:11.5px;display:flex;align-items:center;justify-content:center;gap:8px}

.site-footer{position:absolute;top:860px;left:0;width:998px;height:340px;background:var(--footer);color:var(--footer-text)}
.site-footer h2{font-size:15px;font-weight:400;color:#fff;position:absolute;top:47px}
.contact-info h2{left:73px}
.info-list{position:absolute;left:74px;top:81px;width:260px;list-style:none;font-size:10.6px;line-height:18.5px}
.info-list li{display:flex;gap:8px;margin-bottom:11px}
.info-list svg{flex:none;margin-top:4px}
.divider{position:absolute;left:424px;top:50px;width:1px;height:203px;background:var(--footer-line)}
.contact-form h2{left:517px}
.field{position:absolute;border-bottom:1px solid var(--footer-line)}
.field label{display:block;font-size:12px;color:#fff}
.field .placeholder{display:block;font-size:9.5px;color:#aeb3ba;margin-top:6px;padding-bottom:7px}
.captcha{position:absolute;left:518px;top:217px;width:151px;height:37px;background:#f9f9f9;border:1px solid #d3d3d3;display:flex;align-items:center;padding-left:7px;font-size:7px;color:#222}
.captcha .box{width:13px;height:13px;border:1px solid #c1c1c1;background:#fff;margin-right:7px}
.captcha .mark{position:absolute;right:10px;top:9px;width:14px;height:14px;background:#aab6c8}
.submit{position:absolute;left:829px;top:217px;width:96px;height:37px;background:var(--accent);color:#fff;font-size:12px;display:flex;align-items:center;justify-content:center;gap:14px}
.footer-rule{position:absolute;left:73px;top:297px;width:852px;height:1px;background:var(--footer-line)}
.copyright{position:absolute;top:313px;width:100%;text-align:center;font-size:10.5px;color:#fff}
</style>
</head>
<body>

<header class="site-header">
  <div class="brand"><span class="brand-square"></span>KAVNEX</div>
  <nav class="main-nav">
    <a>About us</a><a>Projects</a><a>Support</a><a>Clients</a><a>Careers</a><a class="active">Testimonials</a><a>Contact</a>
  </nav>
  <svg class="search-icon" width="12" height="12" viewBox="0 0 12 12" fill="none" stroke="#333" stroke-width="1.2"><circle cx="5" cy="5" r="4"/><line x1="8" y1="8" x2="11.5" y2="11.5"/></svg>
</header>

<section class="page-hero" role="img" aria-label="Photo of a team working in a bright office">
  <h1>Customer Testimonials</h1>
  <div class="breadcrumb">Home<span>›</span>Testimonials</div>
</section>

<main class="testimonials">
  <article class="testimonial"><p>In enim justo rhoncus ut imperdiet a venenatis vitae justo nullam dictum felis eu pede mollis pretium integer tincidunt cras dapibus vivam lorem ipsum <span class="tag">#KAVNEX</span></p>
    <div class="author"><div class="avatar" role="img" aria-label="Portrait of Marlow Jennings" style="background:linear-gradient(135deg,#5b7fa8,#2f3d4f)"></div><div><div class="author-name">Marlow Jennings</div><div class="author-handle">@marlow</div></div></div>
    <svg class="quote-mark" width="30" height="22" viewBox="0 0 30 22" fill="#ececec"><path d="M2 12C2 6 5 2 11 1l1 3c-3 1-5 3-5 6h5v10H2zM18 12c0-6 3-10 9-11l1 3c-3 1-5 3-5 6h5v10H18z"/></svg></article>
  <article class="testimonial"><p>In enim justo rhoncus ut imperdiet a venenatis vitae justo nullam dictum felis eu pede mollis pretium integer tincidunt cras dapibus vivam lorem ipsum <span class="tag">#KAVNEX</span></p>
    <div class="author"><div class="avatar" role="img" aria-label="Portrait of Talia Verne" style="background:linear-gradient(135deg,#c9b9a4,#3a8fa6)"></div><div><div class="author-name">Talia Verne</div><div class="author-handle">@talia</div></div></div>
    <svg class="quote-mark" width="30" height="22" viewBox="0 0 30 22" fill="#ececec"><path d="M2 12C2 6 5 2 11 1l1 3c-3 1-5 3-5 6h5v10H2zM18 12c0-6 3-10 9-11l1 3c-3 1-5 3-5 6h5v10H18z"/></svg></article>
  <article class="testimonial"><p>In enim justo rhoncus ut imperdiet a venenatis vitae justo nullam dictum felis eu pede mollis pretium integer tincidunt cras dapibus vivam lorem ipsum <span class="tag">#KAVNEX</span></p>
    <div class="author"><div class="avatar" role="img" aria-label="Portrait of Rowan Ellis" style="background:linear-gradient(135deg,#e8e8e8,#9a9a9a)"></div><div><div class="author-name">Rowan Ellis</div><div class="author-handle">@rowan</div></div></div>
    <svg class="quote-mark" width="30" height="22" viewBox="0 0 30 22" fill="#ececec"><path d="M2 12C2 6 5 2 11 1l1 3c-3 1-5 3-5 6h5v10H2zM18 12c0-6 3-10 9-11l1 3c-3 1-5 3-5 6h5v10H18z"/></svg></article>
  <article class="testimonial"><p>In enim justo rhoncus ut imperdiet a venenatis vitae justo nullam dictum felis eu pede mollis pretium integer tincidunt cras dapibus vivam lorem ipsum <span class="tag">#KAVNEX</span></p>
    <div class="author"><div class="avatar" role="img" aria-label="Portrait of Callum Hart" style="background:linear-gradient(135deg,#ddd6d0,#6b5a55)"></div><div><div class="author-name">Callum Hart</div><div class="author-handle">@callum</div></div></div>
    <svg class="quote-mark" width="30" height="22" viewBox="0 0 30 22" fill="#ececec"><path d="M2 12C2 6 5 2 11 1l1 3c-3 1-5 3-5 6h5v10H2zM18 12c0-6 3-10 9-11l1 3c-3 1-5 3-5 6h5v10H18z"/></svg></article>
  <article class="testimonial"><p>In enim justo rhoncus ut imperdiet a venenatis vitae justo nullam dictum felis eu pede mollis pretium integer tincidunt cras dapibus vivam lorem ipsum <span class="tag">#KAVNEX</span></p>
    <div class="author"><div class="avatar" role="img" aria-label="Portrait of Desmond Fairley" style="background:linear-gradient(135deg,#3a3a3a,#e0b21e)"></div><div><div class="author-name">Desmond Fairley</div><div class="author-handle">@desmond</div></div></div>
    <svg class="quote-mark" width="30" height="22" viewBox="0 0 30 22" fill="#ececec"><path d="M2 12C2 6 5 2 11 1l1 3c-3 1-5 3-5 6h5v10H2zM18 12c0-6 3-10 9-11l1 3c-3 1-5 3-5 6h5v10H18z"/></svg></article>
  <article class="testimonial"><p>In enim justo rhoncus ut imperdiet a venenatis vitae justo nullam dictum felis eu pede mollis pretium integer tincidunt cras dapibus vivam lorem ipsum <span class="tag">#KAVNEX</span></p>
    <div class="author"><div class="avatar" role="img" aria-label="Portrait of Nolan Pryce" style="background:linear-gradient(135deg,#e0a33a,#6a3c12)"></div><div><div class="author-name">Nolan Pryce</div><div class="author-handle">@nolan</div></div></div>
    <svg class="quote-mark" width="30" height="22" viewBox="0 0 30 22" fill="#ececec"><path d="M2 12C2 6 5 2 11 1l1 3c-3 1-5 3-5 6h5v10H2zM18 12c0-6 3-10 9-11l1 3c-3 1-5 3-5 6h5v10H18z"/></svg></article>
  <article class="testimonial"><p>In enim justo rhoncus ut imperdiet a venenatis vitae justo nullam dictum felis eu pede mollis pretium integer tincidunt cras dapibus vivam lorem ipsum <span class="tag">#KAVNEX</span></p>
    <div class="author"><div class="avatar" role="img" aria-label="Portrait of Felix Marsh" style="background:linear-gradient(135deg,#f0f0f0,#1f1f22)"></div><div><div class="author-name">Felix Marsh</div><div class="author-handle">@felix</div></div></div>
    <svg class="quote-mark" width="30" height="22" viewBox="0 0 30 22" fill="#ececec"><path d="M2 12C2 6 5 2 11 1l1 3c-3 1-5 3-5 6h5v10H2zM18 12c0-6 3-10 9-11l1 3c-3 1-5 3-5 6h5v10H18z"/></svg></article>
  <article class="testimonial"><p>In enim justo rhoncus ut imperdiet a venenatis vitae justo nullam dictum felis eu pede mollis pretium integer tincidunt cras dapibus vivam lorem ipsum <span class="tag">#KAVNEX</span></p>
    <div class="author"><div class="avatar" role="img" aria-label="Portrait of Idris Vale" style="background:linear-gradient(180deg,#b9b3ad,#4c4540)"></div><div><div class="author-name">Idris Vale</div><div class="author-handle">@idris</div></div></div>
    <svg class="quote-mark" width="30" height="22" viewBox="0 0 30 22" fill="#ececec"><path d="M2 12C2 6 5 2 11 1l1 3c-3 1-5 3-5 6h5v10H2zM18 12c0-6 3-10 9-11l1 3c-3 1-5 3-5 6h5v10H18z"/></svg></article>
  <article class="testimonial"><p>In enim justo rhoncus ut imperdiet a venenatis vitae justo nullam dictum felis eu pede mollis pretium integer tincidunt cras dapibus vivam lorem ipsum <span class="tag">#KAVNEX</span></p>
    <div class="author"><div class="avatar" role="img" aria-label="Portrait of Soren Patel" style="background:linear-gradient(135deg,#5d6f80,#c8ced4)"></div><div><div class="author-name">Soren Patel</div><div class="author-handle">@soren</div></div></div>
    <svg class="quote-mark" width="30" height="22" viewBox="0 0 30 22" fill="#ececec"><path d="M2 12C2 6 5 2 11 1l1 3c-3 1-5 3-5 6h5v10H2zM18 12c0-6 3-10 9-11l1 3c-3 1-5 3-5 6h5v10H18z"/></svg></article>
</main>

<a class="view-more">View More <svg width="8" height="7" viewBox="0 0 8 7" fill="none" stroke="#fff"><path d="M0 3.5h7M4.5 1l2.5 2.5L4.5 6"/></svg></a>

<footer class="site-footer">
  <section class="contact-info">
    <h2>Contact information</h2>
    <ul class="info-list">
      <li><svg width="9" height="11" viewBox="0 0 9 11" fill="#f7941d"><path d="M4.5 0A4.5 4.5 0 0 0 0 4.5C0 8 4.5 11 4.5 11S9 8 9 4.5A4.5 4.5 0 0 0 4.5 0zm0 6.3a1.8 1.8 0 1 1 0-3.6 1.8 1.8 0 0 1 0 3.6z"/></svg><span>Address:Some address line goes here. City name, Country name here.</span></li>
      <li><svg width="9" height="9" viewBox="0 0 9 9" fill="#f7941d"><path d="M1.8 0l1.6 2-1 1.2a6 6 0 0 0 3.4 3.4l1.2-1L9 7.2 7.6 9C3.4 8.6.4 5.6 0 1.4z"/></svg><span>Phone: 555 014 2368</span></li>
      <li><svg width="9" height="7" viewBox="0 0 9 7" fill="#f7941d"><path d="M0 0h9v7H0zm.8.8L4.5 4 8.2.8z" fill-rule="evenodd"/></svg><span>Email: info@kavnex.com</span></li>
      <li><svg width="9" height="9" viewBox="0 0 9 9" fill="#f7941d"><path d="M2 0h5v2.5H2zM0 3h9v4H7.2v2H1.8V7H0zm2.6 3v2.2h3.8V6z"/></svg><span>Fax: 555 014 2390</span></li>
    </ul>
  </section>
  <div class="divider"></div>
  <section class="contact-form">
    <h2>Contact now</h2>
    <div class="field" style="left:517px;top:88px;width:196px"><label>Name:</label><span class="placeholder">Enter your name...</span></div>
    <div class="field" style="left:728px;top:88px;width:197px"><label>Email:</label><span class="placeholder">Enter your email...</span></div>
    <div class="field" style="left:517px;top:144px;width:408px;height:58px"><label>Message:</label><span class="placeholder">Enter your message...</span></div>
    <div class="captcha"><span class="box"></span>I'm not a robot<span class="mark"></span></div>
    <a class="submit">Submit <svg width="8" height="7" viewBox="0 0 8 7" fill="none" stroke="#fff"><path d="M0 3.5h7M4.5 1l2.5 2.5L4.5 6"/></svg></a>
  </section>
  <div class="footer-rule"></div>
  <p class="copyright">© 2017, All Rights Reserved.</p>
</footer>

</body>
</html>
```